Print Design Project- raffle tickets

We need 10 print designs for raffle tickets.
Please create one or two as per specs and do more only if I get in touch with you.
The tickets will be given out to elementary school kids for eating fruits and veggies at lunch time.
The tickets need to bright, colorful and cool.
They will contain the logo (provided), a clip art image (not photo) of a cool teen as per description attached and text. I will need two versions of the final copy- one with the stub and one without the stub for each ticket.
The ticket size is 5.13" by 1.88"
The safe size is 4.92" by 1.67"
The tear off stub is 1" from the right.
The stubs will be a solid color- red, orange, yellow, green and indigo (bluish-purple)
Updates

Target Market(s)

5-12 year olds

Industry/Entity Type

School

Requirements
Must have
• The given text, logo provided and text provided.
The designer will need to put in appropriate clip art pictures of teenagers doing related activities like snowboarding, gardening, basketball etc.
The pictures should look 'cool'. We are trying to make healthy eating be 'cool' and these tickets should be 'wanted' by all the kids in the cafeteria. This should drive them to eat fruits and veggies. High on fun factor.

```html
<!DOCTYPE html>
<html lang="en">
<head>
<meta charset="utf-8">
<title>Veggie Spectrum Quest – Raffle Ticket</title>
<link rel="stylesheet" href="https://fonts.googleapis.com/css2?family=Chewy&family=Schoolbell&family=Fredoka+One&display=swap">
<style>
  :root {
    --purple-deep: #4f1680;
    --purple: #7a26b0;
    --magenta: #c4218f;
    --pink-glow: #e0409e;
    --stub-green: #82e83c;
    --title-blue: #3b5ff0;
    --outline-blue: #1d3fd0;
    --white: #ffffff;
    --pill-green-top: #9af07a;
    --pill-green: #3fbf2e;
    --pill-green-dark: #2a8f1e;
    --code-blue: #1e8fe8;
    --code-blue-dark: #0b4fa8;
    --skin-pink: #f2a7c8;
    --desk-tan: #c9a24a;
    --hair-tone: #f4c16a;
    --pepper-red: #e8231c;
    --pepper-orange: #f79a12;
    --pepper-green: #69c21e;
  }
  html, body { margin: 0; padding: 0; overflow: hidden; background: #ffffff; }
  .ticket {
    position: relative;
    width: 1200px;
    height: 440px;
    overflow: hidden;
    background: var(--purple);
    font-family: "Schoolbell", "Comic Sans MS", cursive;
  }
  .ticket__backdrop { position: absolute; inset: 0; }
  .ticket__stub {
    position: absolute; top: 0; right: 0;
    width: 240px; height: 440px;
    background: var(--stub-green);
  }
  .brand {
    position: absolute;
    left: 30px; top: 36px;
    width: 162px; height: 366px;
    display: flex; align-items: center; justify-content: center;
  }
  .brand__name {
    transform: rotate(-90deg);
    white-space: nowrap;
    text-align: center;
    font-family: "Fredoka One", "Arial Rounded MT Bold", sans-serif;
    font-size: 34px;
    line-height: 1.15;
    color: var(--white);
  }
  .brand__dot {
    display: inline-block; width: 18px; height: 18px;
    border-radius: 50%; background: var(--white);
    vertical-align: middle; margin-right: 10px;
  }
  .profile {
    position: absolute;
    left: 296px; top: 40px;
    width: 428px;
    text-align: center;
    color: var(--white);
  }
  .profile__title {
    margin: 0 0 4px;
    font-family: "Chewy", "Comic Sans MS", cursive;
    font-weight: 400;
    font-size: 34px;
    line-height: 38px;
    color: var(--title-blue);
    text-shadow: 2px 0 #fff, -2px 0 #fff, 0 2px #fff, 0 -2px #fff, 2px 2px #fff, -2px -2px #fff, 2px -2px #fff, -2px 2px #fff;
  }
  .profile__bio {
    margin: 0;
    font-size: 19px;
    line-height: 27px;
    white-space: nowrap;
    text-shadow: 1px 0 var(--outline-blue), -1px 0 var(--outline-blue), 0 1px var(--outline-blue), 0 -1px var(--outline-blue), 1px 1px var(--outline-blue), -1px -1px var(--outline-blue);
  }
  .site-button {
    position: absolute;
    left: 324px; top: 284px;
    width: 420px; height: 64px;
    border-radius: 32px;
    background: linear-gradient(to bottom, var(--pill-green-top) 0%, var(--pill-green) 55%, var(--pill-green-dark) 100%);
    border: 2px solid #e6ffd8;
    box-sizing: border-box;
    box-shadow: 0 3px 6px rgba(0,0,0,0.35);
    display: flex; align-items: center; justify-content: center;
    font-family: Georgia, "Times New Roman", serif;
    font-size: 36px;
    color: var(--white);
    text-shadow: 0 2px 3px rgba(0,0,0,0.4);
  }
  .access-code {
    position: absolute;
    left: 373px; top: 368px;
    width: 330px; height: 36px;
    background: linear-gradient(to bottom, #4fb6ff, var(--code-blue));
    border: 2px solid var(--code-blue-dark);
    box-sizing: border-box;
    border-radius: 4px;
    display: flex; align-items: center; justify-content: center;
    font-family: Arial, Helvetica, sans-serif;
    font-size: 20px;
    letter-spacing: 0.5px;
    color: var(--white);
  }
  .art { position: absolute; }
  .art--swimmer { left: 210px; top: 170px; width: 118px; height: 180px; }
  .art--writer { left: 740px; top: 6px; width: 180px; height: 236px; }
  .art--peppers { left: 780px; top: 276px; width: 168px; height: 148px; }
</style>
</head>
<body>
<main class="ticket">
  <svg class="ticket__backdrop" width="1200" height="440" viewBox="0 0 1200 440" aria-hidden="true">
    <defs>
      <linearGradient id="bg-base" x1="0" y1="0" x2="1" y2="1">
        <stop offset="0" stop-color="#5a1a92"/>
        <stop offset="0.5" stop-color="#8a2aa8"/>
        <stop offset="1" stop-color="#4f1680"/>
      </linearGradient>
      <linearGradient id="swoosh" x1="0" y1="0" x2="1" y2="0">
        <stop offset="0" stop-color="#b81f96"/>
        <stop offset="0.55" stop-color="#e0409e"/>
        <stop offset="1" stop-color="#a61d8e"/>
      </linearGradient>
      <radialGradient id="glow" cx="0.45" cy="0.5" r="0.5">
        <stop offset="0" stop-color="#ff8fd0" stop-opacity="0.55"/>
        <stop offset="1" stop-color="#ff8fd0" stop-opacity="0"/>
      </radialGradient>
    </defs>
    <rect width="960" height="440" fill="url(#bg-base)"/>
    <path d="M0 150 C 250 90, 500 130, 700 190 S 900 260, 960 230 L 960 440 L 0 440 Z" fill="url(#swoosh)" opacity="0.85"/>
    <path d="M0 250 C 260 200, 520 260, 960 330 L 960 440 L 0 440 Z" fill="#7a1f9a" opacity="0.55"/>
    <ellipse cx="520" cy="230" rx="330" ry="150" fill="url(#glow)"/>
  </svg>

  <div class="ticket__stub" aria-hidden="true"></div>

  <div class="brand">
    <span class="brand__name"><span class="brand__dot"></span>Veggie Spectrum<br>Quest</span>
  </div>

  <section class="profile">
    <h1 class="profile__title">Future author Lila.</h1>
    <p class="profile__bio">
      Loves writing mysteries,<br>
      swimming and bell peppers dipped in hummus.<br>
      This tasty snack keeps her fueled and away from<br>
      writers block! Get her delish<br>
      hummus recipe at
    </p>
  </section>

  <div class="site-button">www.VSQkids.com</div>
  <div class="access-code">Access Code: VSQ 131</div>

  <svg class="art art--swimmer" viewBox="0 0 118 180" role="img" aria-label="Cartoon girl in a pink swim cap and swimsuit with goggles">
    <rect x="6" y="4" width="106" height="172" rx="48" fill="var(--skin-pink)" opacity="0.85"/>
  </svg>

  <svg class="art art--writer" viewBox="0 0 180 236" role="img" aria-label="Cartoon girl with pigtails writing a story at a desk">
    <rect x="0" y="130" width="180" height="100" rx="8" fill="var(--desk-tan)" opacity="0.9"/>
    <rect x="40" y="4" width="110" height="140" rx="45" fill="var(--hair-tone)" opacity="0.85"/>
  </svg>

  <svg class="art art--peppers" viewBox="0 0 168 148" role="img" aria-label="Red, green and orange bell peppers">
    <defs>
      <linearGradient id="pepper-tones" x1="0" y1="0" x2="1" y2="1">
        <stop offset="0" stop-color="var(--pepper-green)"/>
        <stop offset="0.5" stop-color="var(--pepper-red)"/>
        <stop offset="1" stop-color="var(--pepper-orange)"/>
      </linearGradient>
    </defs>
    <rect x="4" y="4" width="160" height="140" rx="58" fill="url(#pepper-tones)"/>
  </svg>
</main>
</body>
</html>
```